Business Card for a Mortgage Agent (myself)

I need a business card for my new job as Mortgage Agent. The Broker's logo is to be on the card as well as the brokerage License number. Not sure if to include a photo or not. Info to be on card.
Dario Fenn
Mortgage Agent
Lic # M37115908
Cell: 555-714-2093
Email: dariofennk.ma@quillpost.com
Web: www.kenhartwellmortgages.com
TQV Brokerage Lic. # 58219

```html
<!DOCTYPE html>
<html lang="en">
<head>
<meta charset="utf-8">
<title>Dario Fenn – Mortgage Agent Business Card</title>
<link rel="stylesheet" href="https://fonts.googleapis.com/css2?family=Jost:ital,wght@0,400;0,500;0,700;1,500&display=swap">
<style>
  :root {
    --stage: #6b6c6e;
    --paper: #eef0f2;
    --paper-shade: #dfe2e6;
    --brand-blue: #0d4a8f;
    --brand-yellow: #f7c600;
    --white: #ffffff;
  }
  * { box-sizing: border-box; margin: 0; padding: 0; }
  html, body {
    width: 667px; height: 1200px; overflow: hidden;
    background: var(--stage);
    font-family: "Jost", "Futura", sans-serif;
  }
  .card {
    position: absolute; left: 30px;
    width: 607px; height: 364px;
    overflow: hidden;
    box-shadow: 0 10px 28px rgba(0,0,0,.35);
  }
  .card--front { top: 216px; }
  .card--back { top: 620px; }
  .card__texture {
    position: absolute; inset: 0;
    background: linear-gradient(160deg, var(--paper) 0%, var(--paper-shade) 50%, var(--paper) 100%);
  }

  /* Brand lockup */
  .brand { position: absolute; text-align: center; color: var(--brand-blue); }
  .brand__mark {
    display: inline-block; background: var(--brand-yellow);
  }
  .brand__name { font-weight: 700; letter-spacing: .12em; display: block; }
  .brand__full { font-weight: 500; display: block; text-transform: uppercase; }
  .brand__licence { font-style: italic; font-weight: 500; display: block; }

  .card--front .brand { left: 0; right: 0; top: 100px; }
  .card--front .brand__mark { width: 42px; height: 42px; margin-bottom: 14px; }
  .card--front .brand__name { font-size: 40px; line-height: 1; }
  .card--front .brand__full { font-size: 17px; margin-top: 12px; letter-spacing: .04em; }
  .card--front .brand__licence { font-size: 12px; margin-top: 6px; padding-left: 160px; }

  .card--back .brand { left: 52px; width: 150px; top: 146px; }
  .card--back .brand__mark { width: 20px; height: 20px; margin-bottom: 6px; }
  .card--back .brand__name { font-size: 17px; line-height: 1; }
  .card--back .brand__full { font-size: 7.5px; margin-top: 5px; }
  .card--back .brand__licence { font-size: 6px; margin-top: 2px; padding-left: 60px; }

  /* Contact panel */
  .contact-panel {
    position: absolute; left: 243px; right: 0; top: 49px; bottom: 47px;
    background: var(--brand-blue);
    border-radius: 12px 0 0 12px;
    color: var(--white);
    padding: 36px 0 0 44px;
  }
  .agent__name { font-size: 20px; line-height: 1.1; font-weight: 400; }
  .agent__name strong { font-weight: 700; }
  .agent__role-row { display: flex; align-items: center; margin-top: 2px; }
  .agent__role { font-size: 11px; font-weight: 400; white-space: nowrap; }
  .agent__rule { flex: 1; height: 1.5px; background: var(--white); margin-left: 6px; }
  .licences { margin-top: 42px; font-size: 11.5px; line-height: 1.55; }
  .contact-list { list-style: none; margin-top: 22px; }
  .contact-list li {
    display: flex; align-items: center; gap: 12px;
    font-size: 13.6px; font-weight: 500; height: 27px;
  }
  .contact-icon {
    width: 20px; height: 20px; border-radius: 50%;
    background: var(--brand-yellow);
    display: flex; align-items: center; justify-content: center; flex: none;
  }
</style>
</head>
<body>

<section class="card card--front" aria-label="Card front">
  <div class="card__texture" role="img" aria-label="Fine flowing wavy line pattern in light grey"></div>
  <div class="brand">
    <span class="brand__mark"></span>
    <span class="brand__name">TQV</span>
    <span class="brand__full">Trusted Quarter Ventures</span>
    <span class="brand__licence">License #58219</span>
  </div>
</section>

<section class="card card--back" aria-label="Card back">
  <div class="card__texture" role="img" aria-label="Fine flowing wavy line pattern in light grey"></div>
  <div class="brand">
    <span class="brand__mark"></span>
    <span class="brand__name">TQV</span>
    <span class="brand__full">Trusted Quarter Ventures</span>
    <span class="brand__licence">License #58219</span>
  </div>

  <div class="contact-panel">
    <h1 class="agent__name"><strong>Dario</strong> Fenn</h1>
    <div class="agent__role-row">
      <span class="agent__role">Mortgage Agent</span>
      <span class="agent__rule"></span>
    </div>
    <p class="licences">Lic # M37115908<br>TQV Brokerage Lic. # 58219</p>
    <ul class="contact-list">
      <li>
        <span class="contact-icon">
          <svg width="11" height="11" viewBox="0 0 24 24" aria-hidden="true"><path fill="#0d4a8f" d="M6.6 10.8a15.1 15.1 0 0 0 6.6 6.6l2.2-2.2a1 1 0 0 1 1-.25 11.4 11.4 0 0 0 3.6.57 1 1 0 0 1 1 1V20a1 1 0 0 1-1 1A17 17 0 0 1 3 4a1 1 0 0 1 1-1h3.5a1 1 0 0 1 1 1c0 1.25.2 2.45.57 3.57a1 1 0 0 1-.25 1z"/></svg>
        </span>555-714-2093
      </li>
      <li>
        <span class="contact-icon">
          <svg width="11" height="11" viewBox="0 0 24 24" aria-hidden="true"><rect x="3" y="5" width="18" height="14" rx="1.5" fill="none" stroke="#0d4a8f" stroke-width="2.2"/><path d="M3.5 6l8.5 7 8.5-7" fill="none" stroke="#0d4a8f" stroke-width="2.2"/></svg>
        </span>dariofennk.ma@quillpost.com
      </li>
      <li>
        <span class="contact-icon">
          <svg width="12" height="12" viewBox="0 0 24 24" aria-hidden="true"><g fill="none" stroke="#0d4a8f" stroke-width="2"><circle cx="12" cy="12" r="9"/><ellipse cx="12" cy="12" rx="4" ry="9"/><path d="M3 12h18"/></g></svg>
        </span>www.kenhartwellmortgages.com
      </li>
    </ul>
  </div>
</section>

</body>
</html>
```